Banner design

I need a banner designed that we will be putting on our gym walls. We need two banners but both will have the same design:
- One will be printed 12.2 X 2.5m
- One will be printed 9.4 X 2.5m
We are a kids gymnastics and cheerleading gym so are looking for something bright and fun that still looks professional.
Our colours are lime green, navy blue and white.
I have uploaded a couple of examples of what other gyms have done.
Kids

```html
<!DOCTYPE html>
<html lang="en">
<head>
<meta charset="utf-8">
<title>Vaulta Gymsports Wall Banner</title>
<link href="https://fonts.googleapis.com/css2?family=Roboto:wght@400;500;700;900&family=Roboto+Condensed:wght@400;700&display=swap" rel="stylesheet">
<style>
  :root {
    --page: #ffffff;
    --banner-white: #ffffff;
    --forest: #2e5c4b;
    --forest-light: #3f7862;
    --navy: #1e2b57;
    --lime: #5cb531;
    --text-light: #ffffff;
    --rule: rgba(255,255,255,0.6);
    --photo-warm: #efe4dc;
    --photo-cool: #dfe9f2;
  }
  html, body {
    margin: 0;
    width: 974px;
    height: 1200px;
    overflow: hidden;
    background: var(--page);
  }
  .canvas {
    position: relative;
    width: 974px;
    height: 1200px;
  }
  .banner {
    position: absolute;
    left: 81px;
    top: 515px;
    width: 812px;
    height: 170px;
    background: var(--banner-white);
    box-shadow: 0 8px 24px rgba(0,0,0,0.28);
    overflow: hidden;
  }
  .banner-art {
    display: block;
    width: 812px;
    height: 170px;
  }
  .brand-name {
    font-family: "Roboto", Arial, sans-serif;
    font-weight: 900;
    fill: var(--navy);
  }
  .brand-url {
    font-family: "Roboto", Arial, sans-serif;
    font-weight: 500;
    fill: var(--navy);
    letter-spacing: 1.5px;
  }
  .headline {
    font-family: "Roboto", Arial, sans-serif;
    font-weight: 900;
    fill: var(--text-light);
  }
  .subline {
    font-family: "Roboto Condensed", Arial, sans-serif;
    font-weight: 700;
    fill: var(--text-light);
  }
</style>
</head>
<body>
<main class="canvas">
  <section class="banner" aria-label="Vaulta Gymsports wall banner">
    <svg class="banner-art" viewBox="0 0 1015 212" xmlns="http://www.w3.org/2000/svg">
      <defs>
        <radialGradient id="panelGlow" cx="0.5" cy="0.45" r="0.6">
          <stop offset="0" stop-color="var(--forest-light)"/>
          <stop offset="1" stop-color="var(--forest)"/>
        </radialGradient>
        <linearGradient id="photoFade" x1="0" y1="0" x2="1" y2="0">
          <stop offset="0" stop-color="#ffffff"/>
          <stop offset="0.18" stop-color="var(--photo-warm)"/>
          <stop offset="0.6" stop-color="var(--photo-cool)"/>
          <stop offset="1" stop-color="#e9e9ec"/>
        </linearGradient>
      </defs>

      <g class="photo-area" role="img" aria-label="Photo of smiling children and an adult stretching over red, blue and yellow exercise balls">
        <rect x="700" y="0" width="315" height="212" fill="url(#photoFade)"/>
      </g>

      <polygon class="message-panel" points="293,0 725,0 640,212 215,212" fill="url(#panelGlow)"/>

      <g class="panel-stripes" stroke-linecap="round" stroke-width="13">
        <g stroke="var(--forest)">
          <line x1="278" y1="10" x2="258" y2="58"/>
          <line x1="300" y1="26" x2="286" y2="60"/>
          <line x1="232" y1="150" x2="218" y2="186"/>
          <line x1="248" y1="196" x2="244" y2="206"/>
          <line x1="738" y1="12" x2="705" y2="92"/>
          <line x1="752" y1="36" x2="720" y2="114"/>
          <line x1="708" y1="0" x2="708" y2="0"/>
        </g>
        <g stroke="var(--banner-white)">
          <line x1="318" y1="12" x2="296" y2="66"/>
          <line x1="246" y1="150" x2="232" y2="186"/>
          <line x1="722" y1="8" x2="706" y2="46"/>
          <line x1="660" y1="130" x2="634" y2="194"/>
          <line x1="690" y1="150" x2="664" y2="212"/>
          <line x1="710" y1="186" x2="700" y2="210"/>
        </g>
      </g>

      <g class="brand">
        <circle cx="42" cy="86" r="10" fill="var(--lime)"/>
        <text class="brand-name" x="60" y="96" font-size="29">VAULTA</text>
        <text class="brand-name" x="24" y="140" font-size="24">GYMSPORTS</text>
        <text class="brand-url" x="24" y="165" font-size="11">www.vaultagym.com</text>
      </g>

      <g class="message">
        <text class="headline" x="341" y="87" font-size="29">WE ARE A KIDS</text>
        <text class="headline" x="341" y="116" font-size="29">GYMNASTICS</text>
        <text class="subline" x="341" y="138" font-size="20">AND CHEERLEADING GYM</text>
        <line x1="341" y1="153" x2="455" y2="153" stroke="var(--rule)" stroke-width="1"/>
        <line x1="471" y1="153" x2="587" y2="153" stroke="var(--rule)" stroke-width="1"/>
        <polygon points="463,147 465,151 469,151 466,154 467,158 463,156 459,158 460,154 457,151 461,151" fill="none" stroke="var(--text-light)" stroke-width="1"/>
      </g>
    </svg>
  </section>
</main>
</body>
</html>
```